Copper Mist Informational brochure

Creative and attractive brochure with product information, instructions, and self care.

Copper Mist:
We are a cannabis vape company located in California. Our vape cartridges are pre-filled with our award winning oil for the most discreet and convenient way for patients to medicate.

-The brochure/ informational card will have the same similar design/ scheme as the product packaging.

Content:

---------------------
"Copper Mist

Unlike many other extraction processes, our oil is SOLVENT-FREE with absolutely NO additives or harmful chemicals. All of our extractions are strain specific and lab tested for potency, residuals, and most importantly CONSISTENCY.

Our vapes are specifically designed to be discreet yet incredibly effective for everyday use.

It's simple. NO butane, NO glycol, NO glycerin. Just pure cannabis oil made in California"

"Voted Best Oil at 2015 Leafmeet in San Bernardino and San Francisco"

---------------------
KNOW THE DIFFERENCE

Butane is a highly volatile and flammable gas used for cannabis extractions also known as "BHO" extractions very popular in today's industry. These extractions are not only dangerous, but also contain chemical contaminants that could present health hazards and cause harmful nodules in the lungs that increase chances of getting infections. When done improperly, harmful chemical solvents are left over for the consumers to smoke, which can cause detrimental long-term health effects.

---------------------
"WHAT IS THC?

THC, or "tetrahydrocannabinol," is the chemical responsible for most of marijuana's psychological effects. It acts much like the cannabinoid chemicals made naturally by the body.

Cannabinoid receptors are concentrated in certain areas of the brain associated with thinking, memory, pleasure, coordination, and time perception. THC attaches to these receptors and activates them.

THC is one of many compounds found in the resin secreted by glands of the marijuana plant. More of these glands are found around the reproductive organs of the plant than on any other area of the plant. Other compounds unique to marijuana, called cannabinoids, are present in this resin. One cannabinoid, CBD is non-psychoactive and actually blocks the high associated with THC.

WHAT IS CBD?

CBD is one of over 60 compounds found in cannabis that belongs to a class of molecules called "cannabinoids." CBD from cannabis is non-psychoactive or less psychoactive than THC-dominant strains, making it an appealing option for patients looking for relief from inflammation, pain, anxiety, psychosis, seizures, spasms, and other conditions without disconcerting feelings of lethargy or dysphoria. CBD has demonstrable neuroprotective and neurogenic effects, and its anti-cancer properties are currently being investigated at several academic research centers in the United States and elsewhere."
---------------------

"Cleaning & Care

Store vape cartridges flat or upright in cool or room temperature to prevent leakage. Exposure to excessive heat may cause the viscosity of the oil to change.

Please refer to our ClipStream (https://lnk.example-short.test/Qm7TpZ) page for videos on proper storage and refill instructions!

Instagram logo with ID:
CopperMist_

Facebook logo with ID
CopperMistGoodsCo

Email:
contact@coppermist.test

ClipStream
Copper Mis (https://lnk.example-short.test/Qm7TpZ)

```html
<!DOCTYPE html>
<html lang="en">
<head>
<meta charset="utf-8">
<title>Copper Mist – Informational Card</title>
<link href="https://fonts.googleapis.com/css2?family=Quicksand:wght@700&family=Nunito:wght@700;800&display=swap" rel="stylesheet">
<style>
  :root {
    --magenta: #d8005a;
    --magenta-soft: rgba(232, 110, 150, 0.35);
    --white: #ffffff;
    --ink: #3a3236;
    --page-bg: #e9edee;
  }
  html, body {
    margin: 0;
    padding: 0;
    width: 1200px;
    height: 1200px;
    overflow: hidden;
    background: var(--page-bg);
    font-family: "Quicksand", sans-serif;
  }
  .card {
    position: absolute;
    left: 203px;
    top: 40px;
    width: 734px;
    height: 1037px;
    background: var(--white);
    transform: scale(1.08);
    transform-origin: top left;
    overflow: hidden;
  }
  .card__shapes {
    position: absolute;
    inset: 0;
  }
  .brand-name {
    position: absolute;
    top: 92px;
    left: 0;
    width: 100%;
    text-align: center;
    margin: 0;
    color: var(--magenta);
    font-family: "Nunito", sans-serif;
    font-weight: 800;
    font-size: 50px;
    letter-spacing: 1px;
    line-height: 1;
  }
  .sparkle-area {
    position: absolute;
    border-radius: 50%;
    background: radial-gradient(circle, var(--magenta-soft) 0%, rgba(232,110,150,0) 70%);
  }
  .sparkle-area--right { left: 600px; top: 310px; width: 120px; height: 130px; }
  .sparkle-area--left { left: 20px; top: 370px; width: 90px; height: 160px; }
  .section-title {
    position: absolute;
    top: 292px;
    left: 0;
    width: 304px;
    height: 61px;
    margin: 0;
    padding-left: 68px;
    box-sizing: border-box;
    line-height: 61px;
    color: var(--magenta);
    font-weight: 700;
    font-size: 17px;
    letter-spacing: 0.3px;
  }
  .cbd-text {
    position: absolute;
    top: 371px;
    left: 72px;
    width: 612px;
    margin: 0;
    color: var(--white);
    font-weight: 700;
    font-size: 11px;
    line-height: 15px;
    letter-spacing: 0.35px;
  }
  .cbd-text p { margin: 0 0 15px; }
  .care {
    position: absolute;
    top: 572px;
    left: 67px;
    width: 535px;
    color: var(--magenta);
    font-weight: 700;
    font-size: 11px;
    line-height: 15px;
    letter-spacing: 0.35px;
  }
  .care p { margin: 0 0 15px; }
  .contacts {
    position: absolute;
    top: 757px;
    left: 73px;
    margin: 0;
    padding: 0;
    list-style: none;
  }
  .contacts__item {
    display: flex;
    align-items: center;
    height: 40px;
    margin-bottom: 13px;
    color: var(--ink);
    font-family: "Nunito", sans-serif;
    font-weight: 700;
    font-size: 15px;
  }
  .contacts__icon {
    width: 40px;
    height: 40px;
    border-radius: 50%;
    background: var(--magenta);
    margin-right: 18px;
    flex: none;
  }
</style>
</head>
<body>
  <article class="card">
    <svg class="card__shapes" width="734" height="1037" viewBox="0 0 734 1037" aria-hidden="true">
      <path d="M0 81 Q367 367 734 81 L734 499 L430 499 L430 554 L0 554 Z" fill="var(--magenta)"/>
      <rect x="0" y="292" width="304" height="61" fill="var(--white)"/>
      <rect x="0" y="697" width="734" height="26" fill="var(--magenta)"/>
      <rect x="0" y="1001" width="734" height="36" fill="var(--magenta)"/>
    </svg>

    <h1 class="brand-name">Copper Mist</h1>

    <div class="sparkle-area sparkle-area--right" role="img" aria-label="Soft scattered dot and star decoration"></div>
    <div class="sparkle-area sparkle-area--left" role="img" aria-label="Soft scattered dot decoration"></div>

    <h2 class="section-title">WHAT IS CBD?</h2>
    <div class="cbd-text">
      <p>CBD is one of over 60 compounds found in cannabis that belongs to a class of molecules called "cannabinoids." CBD from cannabis is non-psychoactive or less psychoactive than THC-dominant strains, making it an appealing option for patients looking for relief from inflammation, pain, anxiety, psychosis, seizures, spasms, and other conditions without disconcerting feelings of lethargy</p>
      <p>or dysphoria. CBD has demonstrable neuroprotective and neurogenic effects, and its anti-cancer properties are currently being investigated at several academic research centers in the United States and elsewhere."</p>
    </div>

    <section class="care">
      <p>"Cleaning &amp; Care</p>
      <p>Store vape cartridges flat or upright in cool or room temperature to prevent leakage. Exposure to excessive heat may cause the viscosity of the oil to change.</p>
      <p>Please refer to our ClipStream (https://lnk.example-short.test/Qm7TpZ) page for videos on proper storage and refill instructions!</p>
    </section>

    <ul class="contacts">
      <li class="contacts__item"><span class="contacts__icon"></span>CopperMist_</li>
      <li class="contacts__item"><span class="contacts__icon"></span>CopperMistGoodsCo</li>
      <li class="contacts__item"><span class="contacts__icon"></span>Copper Mis (https://lnk.example-short.test/Qm7TpZ)</li>
      <li class="contacts__item"><span class="contacts__icon"></span>contact@coppermist.test</li>
    </ul>
  </article>
</body>
</html>
```